Building Design company needing a letterhead

We need a letter head for our Building Design company to send letters etc. to our clients, consultants, councils etc. We would like to see our logo used and company colours. I have attached our style guide and an example of our current letterheads. Top left we would like our logo, top right we would like the company details and at the footer we would like some sort of image/design etc. that suits our brand. I like the Torvik Design letterhead attached.

Target Market(s)

Professionals, Councils, Consultants, Mums & Dads

Industry/Entity Type

Architecture

Font styles to use
Other font styles liked:
• refer the design style guide

Colors
f37122
000000
1b1b1b

Requirements
Must have
• Must have the minimum of a logo, company details and footer
Nice to have
• An image/design made for the footer that would suite our brand and website at www.quarvedesign.com.au. Also it would be nice to include the GMKLE logo somewhere perhaps included in the footer.
Should not have
• Large images in the header. I just want the logo and company details.

```html
<!DOCTYPE html>
<html lang="en">
<head>
<meta charset="utf-8">
<title>Quarve Design Letterhead</title>
<link href="https://fonts.googleapis.com/css2?family=Arimo:wght@400;700&family=Carlito&display=swap" rel="stylesheet">
<style>
  :root {
    --brand-orange: #e05a28;
    --ink: #1b1b1b;
    --black: #000000;
    --paper: #f7f7f7;
    --backdrop: #e4e1dc;
  }
  html, body {
    margin: 0;
    padding: 0;
    width: 1189px;
    height: 1200px;
    overflow: hidden;
    background: var(--backdrop);
  }
  .letterhead {
    position: absolute;
    left: 131px;
    top: 0;
    width: 927px;
    height: 1200px;
    background: var(--paper);
    font-family: "Arimo", Arial, sans-serif;
    color: var(--ink);
  }
  .brand {
    position: absolute;
    left: 85px;
    top: 60px;
    display: flex;
    align-items: center;
    gap: 22px;
  }
  .brand-square {
    width: 96px;
    height: 96px;
    background: var(--brand-orange);
  }
  .brand-name {
    font-family: "Arimo", Arial, sans-serif;
    font-weight: 700;
    font-size: 54px;
    line-height: 56px;
    letter-spacing: 3px;
    color: var(--ink);
    text-transform: uppercase;
  }
  .company-details {
    position: absolute;
    right: 76px;
    top: 64px;
    text-align: right;
    font-family: "Carlito", "Calibri", sans-serif;
    font-size: 15.5px;
    line-height: 19px;
    color: var(--black);
  }
  .company-details .gap { margin-left: 14px; }
  .letter-body {
    position: absolute;
    left: 75px;
    top: 289px;
    width: 780px;
    font-size: 16.6px;
    line-height: 27.4px;
    color: var(--ink);
  }
  .letter-body p { margin: 0 0 27.4px; }
  .letter-body p.section-break { margin-top: 54.8px; }
  .footer-band {
    position: absolute;
    left: 0;
    top: 1058px;
    width: 781px;
    height: 95px;
    background: var(--brand-orange);
  }
  .partner-mark {
    position: absolute;
    left: 801px;
    top: 1060px;
    width: 76px;
    display: flex;
    flex-direction: column;
    align-items: center;
    gap: 6px;
  }
  .partner-square {
    width: 66px;
    height: 66px;
    border: 3px solid var(--brand-orange);
    box-sizing: border-box;
  }
  .partner-name {
    font-family: "Arimo", Arial, sans-serif;
    font-size: 16px;
    letter-spacing: 1px;
    color: var(--brand-orange);
  }
</style>
</head>
<body>
<main class="letterhead">
  <header>
    <div class="brand">
      <div class="brand-square"></div>
      <div class="brand-name">Quarve<br>Design</div>
    </div>
    <address class="company-details" style="font-style:normal">
      admin@quarvedesign.com.au<br>
      www.quarvedesign.com.au<br>
      Unit 4/22 Harlow Way Seabrook WA 6300<br>
      PO Box 3187 Seabrook North WA 6300<br>
      PH (08) 5550 0123<span class="gap">ABN 11 222 333 444</span>
    </address>
  </header>

  <section class="letter-body">
    <p>Lorem Ipsum is simply dummy text of the printing and typesetting industry. Lorem Ipsum has been the industry’s standard dummy text ever since the 1500s, when an unknown printer took a galley of type and scrambled it to make a type specimen book. It has survived not only five centuries, but also the leap into electronic typesetting, remaining essentially unchanged. It was popularised in the 1960s with the release of Lettrafix sheets containing Lorem Ipsum passages, and more recently with desktop publishing software like PageForge including versions of Lorem Ipsum.</p>
    <p>It is a long established fact that a reader will be distracted by the readable content of a page when looking at its layout. The point of using Lorem Ipsum is that it has a more-or-less normal distribution of letters, as opposed to using ’Content here, content here’, making it look like readable English. Many desktop publishing packages and web page editors now use Lorem Ipsum as their default model text, and a search for ’lorem ipsum’ will uncover many web sites still in their infancy. Various versions have evolved over the years, sometimes by accident, sometimes on purpose (injected humour and the like).</p>
    <p class="section-break">Contrary to popular belief, Lorem Ipsum is not simply random text. It has roots in a piece of classical Latin literature from 45 BC, making it over 2000 years old. Edwin Harrow, a Latin professor at Ashcombe College in Virginia, looked up one of the more obscure Latin words, consectetur, from a Lorem Ipsum passage, and going through the cites of the word in classical literature, discovered the undoubtable source. Lorem Ipsum comes from sections 1.10.32 and 1.10.33 of "de Finibus Bonorum et Malorum" structures, to generate Lorem Ipsum which looks reasonable. The generated Lorem Ipsum is therefore always free from repetition, injected humour, or non-characteristic words etc.</p>
  </section>

  <footer>
    <div class="footer-band"></div>
    <div class="partner-mark">
      <div class="partner-square"></div>
      <div class="partner-name">GMKLE</div>
    </div>
  </footer>
</main>
</body>
</html>
```